Simple and Clean business card design

We would like the design to be simple clean and to incorporate our colors.

We are open to your design and talent, we have the dots in our logo as we think of it as data points and we connect data points for people.

We are open to see the great creative and clean design you bring to the table

Contact Information for Business Card

please include: name, position, email, phone and website

Font styles to use
Sans Serif

Requirements
Must have
• my colors incorporated, simplicity
Nice to have
• lots of white space, simplicity
Should not have
• complexicity/ complex art

```html
<!DOCTYPE html>
<html lang="en">
<head>
<meta charset="UTF-8">
<title>Dotwell Business Card</title>
<link rel="stylesheet" href="https://fonts.googleapis.com/css2?family=Questrial&display=swap">
<style>
  :root {
    --brand-blue: #4d78bf;
    --card-white: #ffffff;
    --ink: #1a1a1a;
    --backdrop: #e6e9ec;
    --shadow: rgba(20, 30, 45, 0.18);
  }
  * { margin: 0; padding: 0; box-sizing: border-box; }
  html, body {
    width: 1200px;
    height: 960px;
    overflow: hidden;
    background: var(--backdrop);
    font-family: "Questrial", "Century Gothic", sans-serif;
  }
  .sheet {
    width: 1200px;
    height: 960px;
    display: flex;
    flex-direction: column;
    align-items: center;
    justify-content: center;
    gap: 60px;
  }
  .card {
    width: 560px;
    height: 320px;
    box-shadow: 0 10px 28px var(--shadow);
    position: relative;
  }
  .card-front {
    background: var(--brand-blue);
    display: flex;
    align-items: center;
    justify-content: center;
  }
  .front-mark {
    display: flex;
    align-items: center;
    gap: 14px;
    color: var(--card-white);
    font-size: 44px;
    letter-spacing: 1px;
  }
  .front-mark .dot {
    width: 22px;
    height: 22px;
    border-radius: 50%;
    background: var(--card-white);
  }
  .card-back {
    background: var(--card-white);
    display: flex;
    flex-direction: column;
    align-items: center;
    padding-top: 46px;
  }
  .wordmark {
    font-size: 54px;
    color: var(--ink);
    line-height: 1;
    letter-spacing: 1px;
  }
  .holder-name {
    margin-top: 10px;
    font-size: 22px;
    letter-spacing: 2px;
    color: var(--ink);
  }
  .contact-list {
    list-style: none;
    margin-top: 26px;
    display: flex;
    flex-direction: column;
    gap: 4px;
  }
  .contact-item {
    display: flex;
    align-items: center;
    gap: 10px;
    font-size: 15px;
    letter-spacing: 3px;
    color: var(--ink);
  }
  .contact-icon {
    width: 15px;
    height: 15px;
    flex: none;
  }
</style>
</head>
<body>
<main class="sheet">
  <section class="card card-front" aria-label="Card front">
    <div class="front-mark">
      <span class="dot"></span>
      <span class="brand-name">Dotwell</span>
    </div>
  </section>

  <section class="card card-back" aria-label="Card back">
    <h1 class="wordmark">Dotwell</h1>
    <p class="holder-name">Name</p>
    <ul class="contact-list">
      <li class="contact-item">
        <svg class="contact-icon" viewBox="0 0 16 16" aria-hidden="true">
          <circle cx="8" cy="6" r="4.2" fill="none" stroke="#1a1a1a" stroke-width="2"/>
          <path d="M8 10.5 V15" stroke="#1a1a1a" stroke-width="2"/>
        </svg>
        <span>position</span>
      </li>
      <li class="contact-item">
        <svg class="contact-icon" viewBox="0 0 16 16" aria-hidden="true">
          <circle cx="8" cy="8" r="2.6" fill="none" stroke="#1a1a1a" stroke-width="1.6"/>
          <path d="M10.6 5.5 V9.6 a1.8 1.8 0 0 0 3.6 0 V8 a6.2 6.2 0 1 0 -2.4 4.9" fill="none" stroke="#1a1a1a" stroke-width="1.6"/>
        </svg>
        <span>email</span>
      </li>
      <li class="contact-item">
        <svg class="contact-icon" viewBox="0 0 16 16" aria-hidden="true">
          <circle cx="8" cy="8" r="7.5" fill="#1a1a1a"/>
          <path d="M5.2 4.4 l1.4 -0.3 l0.9 2 l-0.9 0.8 q0.8 1.7 2.4 2.5 l0.8 -0.9 l2 0.9 l-0.3 1.4 q-4.8 0.4 -6.3 -6.4z" fill="#ffffff"/>
        </svg>
        <span>phone</span>
      </li>
      <li class="contact-item">
        <svg class="contact-icon" viewBox="0 0 16 16" aria-hidden="true">
          <circle cx="8" cy="8" r="7.5" fill="#1a1a1a"/>
          <path d="M1 8 H15 M8 1 V15 M2.5 4.5 H13.5 M2.5 11.5 H13.5" stroke="#ffffff" stroke-width="1"/>
          <ellipse cx="8" cy="8" rx="3.2" ry="7" fill="none" stroke="#ffffff" stroke-width="1"/>
        </svg>
        <span>website</span>
      </li>
    </ul>
  </section>
</main>
</body>
</html>
```